Whitmore Business Card Design

The name of the business is Dara Whitmore, CPA LLC
The service that we offer is Accounting, Tax & Consulting Services. I need it to have the following items:
Dara Whitmore, Principal
Phone Number
Email Address
Physical Address

I have attached the company logo, one in black and one in white. Please provide a design in black background and the other in white background. Please include "Accounting, Tax & Consulting Services". I want the business card to be clean and very professional.

```html
<!DOCTYPE html>
<html lang="en">
<head>
<meta charset="utf-8">
<title>Dara Whitmore, CPA LLC – Business Card</title>
<link rel="stylesheet" href="https://fonts.googleapis.com/css2?family=Roboto:wght@300;400;500&display=swap">
<style>
  :root {
    --brand-red: #961a1f;
    --ink-dark: #3a3a3c;
    --ink-text: #444446;
    --paper: #ffffff;
    --canvas: #f7f7f7;
  }
  * { box-sizing: border-box; margin: 0; padding: 0; }
  html, body { width: 800px; height: 1200px; overflow: hidden; }
  body {
    background: var(--canvas);
    font-family: "Roboto", Arial, sans-serif;
    position: relative;
  }
  .card {
    position: absolute;
    left: 100px;
    width: 600px;
    height: 343px;
    overflow: hidden;
    box-shadow: 0 2px 8px rgba(0,0,0,0.12);
  }
  .card--front { top: 237px; background: var(--paper); }
  .card--back { top: 620px; background: var(--brand-red); }

  .top-band {
    position: absolute; left: 0; top: 0;
    width: 100%; height: 39px;
    background: var(--ink-dark);
  }
  .service-band {
    position: absolute; left: 0; bottom: 0;
    width: 100%; height: 61px;
    background: var(--brand-red);
    color: var(--paper);
    font-size: 15px; font-weight: 500;
    display: flex; align-items: center; justify-content: center;
    letter-spacing: 0.1px;
  }

  .brand-lockup {
    position: absolute;
    left: 50px; top: 80px;
    width: 220px; height: 161px;
    display: flex; align-items: center; gap: 10px;
  }
  .brand-mark {
    width: 14px; height: 14px; flex: none;
    background: var(--brand-red);
  }
  .brand-name {
    font-size: 17px; font-weight: 500;
    color: var(--ink-dark);
    line-height: 1.3;
  }

  .divider {
    position: absolute;
    left: 298px; top: 80px;
    width: 2px; height: 161px;
    background: var(--brand-red);
  }

  .identity { position: absolute; left: 324px; top: 76px; }
  .person-name {
    font-size: 27px; font-weight: 400;
    color: var(--brand-red);
    line-height: 1.1;
  }
  .person-role {
    font-size: 16px; font-weight: 300;
    color: var(--ink-text);
    margin-top: 1px;
  }

  .contact-list {
    position: absolute; left: 323px; top: 157px;
    list-style: none;
    font-size: 16px; font-weight: 300;
    color: var(--ink-text);
    line-height: 1.05;
  }
  .contact-item { display: flex; align-items: center; gap: 10px; margin-bottom: 10px; }
  .contact-icon { width: 10px; height: 10px; flex: none; fill: var(--brand-red); }

  .back-lockup {
    position: absolute; inset: 0;
    display: flex; align-items: center; justify-content: center; gap: 14px;
    color: var(--paper);
  }
  .back-mark { width: 18px; height: 18px; background: var(--paper); }
  .back-name { font-size: 26px; font-weight: 500; letter-spacing: 0.3px; }
</style>
</head>
<body>
  <section class="card card--front" aria-label="Business card front">
    <div class="top-band"></div>

    <div class="brand-lockup">
      <span class="brand-mark"></span>
      <span class="brand-name">Dara Whitmore, CPA LLC</span>
    </div>

    <div class="divider"></div>

    <div class="identity">
      <h1 class="person-name">DARA WHITMORE</h1>
      <p class="person-role">Principal</p>
    </div>

    <ul class="contact-list">
      <li class="contact-item">
        <svg class="contact-icon" viewBox="0 0 10 10" aria-hidden="true">
          <path d="M2 0.5 L3.6 0.5 L4.2 3 L3 3.8 Q3.9 5.9 6 7 L6.8 5.8 L9.4 6.4 L9.4 8 Q9.4 9.5 8 9.5 Q1 9 0.5 2 Q0.5 0.5 2 0.5 Z"/>
        </svg>
        <span>123-456-7890</span>
      </li>
      <li class="contact-item">
        <svg class="contact-icon" viewBox="0 0 10 12" aria-hidden="true" style="height:12px">
          <path d="M5 0 A4 4 0 0 1 9 4 C9 7 5 12 5 12 C5 12 1 7 1 4 A4 4 0 0 1 5 0 Z M5 2.6 A1.4 1.4 0 1 0 5 5.4 A1.4 1.4 0 1 0 5 2.6 Z"/>
        </svg>
        <span>123 NW Somewhere St.<br>Somewhere City, 1111</span>
      </li>
      <li class="contact-item">
        <svg class="contact-icon" viewBox="0 0 12 9" aria-hidden="true" style="width:12px;height:9px">
          <path d="M0 0 H12 V1 L6 5 L0 1 Z M0 2.4 L6 6.4 L12 2.4 V9 H0 Z"/>
        </svg>
        <span>your@email.com</span>
      </li>
    </ul>

    <div class="service-band">Accounting, Tax and Consulting Services</div>
  </section>

  <section class="card card--back" aria-label="Business card back">
    <div class="back-lockup">
      <span class="back-mark"></span>
      <span class="back-name">DARA WHITMORE, CPA LLC</span>
    </div>
  </section>
</body>
</html>
```